Purchase Protection Subscription Program needs a refreshed website

We are refreshing an existing website www.carevaultplus.example. This is a purchase protection product which allows its members to receive extended warranty on the items they buy, receive a rebate of 50% on a repair of an item, a personal shopping concierge, etc. We are looking for a fresh, clean approach - with mass appeal to both men and woman. The site should convey trust, and ease of use.

Thanks to everyone who posted designs. Amazing work! It was a very difficult decision!

```html
<!DOCTYPE html>
<html lang="en">
<head>
<meta charset="utf-8">
<title>CareVaultPlus – Purchase Protection</title>
<link rel="stylesheet" href="https://fonts.googleapis.com/css2?family=Source+Sans+Pro:wght@400;600&family=Yanone+Kaffeesatz:wght@400;600&family=Montserrat:wght@500&family=Nunito:wght@800&family=Open+Sans:wght@400;600;700&display=swap">
<style>
:root{
  --ink:#4a4a4a;
  --ink-soft:#666;
  --brand-red:#e8080d;
  --navy:#1c4e73;
  --orange:#e8772e;
  --date-orange:#f26a10;
  --teal-top:#7ed0c6;
  --teal-bottom:#4fb3a8;
  --footer:#2b2b2b;
  --footer-base:#1f1f1f;
  --footer-text:#e6e6e6;
  --link-blue:#3aa0e8;
  --white:#fff;
}
*{margin:0;padding:0;box-sizing:border-box}
html,body{width:676px;height:1200px;overflow:hidden;background:var(--white)}
body{position:relative;font-family:"Open Sans",sans-serif;color:var(--ink)}
.abs{position:absolute}

.logo{left:90px;top:18px;font-family:"Source Sans Pro",sans-serif;font-size:16px;color:var(--ink-soft)}
.top-links{left:452px;top:14px;font-size:9.5px;color:var(--ink);display:flex;align-items:center;gap:6px}
.top-links .sep{color:#bbb}
.phone-icon{width:11px;height:11px;background:var(--brand-red);border-radius:2px;display:inline-flex;align-items:center;justify-content:center}
.main-nav{top:42px;left:0;width:676px;font-size:9.5px;color:var(--ink-soft)}
.main-nav a{position:absolute;color:inherit;text-decoration:none}
.main-nav .active{color:#222}
.main-nav .active::after{content:"";position:absolute;left:0;right:0;top:14px;height:2px;background:var(--brand-red)}

.hero{left:86px;top:65px;width:509px;height:283px;background:linear-gradient(135deg,#c9a98c 0%,#a88468 35%,#7d8c7a 65%,#b8aea0 100%)}
.slider-arrow{top:196px;width:30px;height:38px}
.slider-dots{top:324px;left:0;width:676px;display:flex;justify-content:center;gap:5px}
.slider-dots span{width:13px;height:13px;border-radius:50%;background:#bbb;border:2px solid #fff}
.slider-dots .current{background:#1c5a66}

.tagline{top:382px;left:0;width:676px;text-align:center;font-family:"Source Sans Pro",sans-serif;font-weight:600;font-size:24px;line-height:29px;color:var(--ink)}
.tagline .brand{color:var(--brand-red)}
.cta{left:275px;top:471px;width:127px;height:29px;background:var(--navy);border-radius:3px;color:#fff;font-family:"Montserrat",sans-serif;font-size:12px;display:flex;align-items:center;justify-content:center}
.divider{left:73px;top:536px;width:532px;height:6px;border-radius:50%;box-shadow:0 4px 6px rgba(0,0,0,.18)}

.feature{top:574px;width:170px}
.feature .ring{width:54px;height:54px;border:2.5px solid var(--orange);border-radius:50%;margin:0 auto;display:flex;align-items:center;justify-content:center}
.feature h3{font-family:"Yanone Kaffeesatz",sans-serif;font-weight:400;font-size:12.5px;color:#222;text-align:center;margin-top:10px}
.feature p,.feature li{font-size:5.6px;line-height:9px;color:#333}
.feature p{margin:10px 14px 0}
.feature ul{list-style:none;margin:3px 0 0 26px}
.feature li::before{content:"›";color:var(--orange);font-weight:700;margin-right:5px}
.small-btn{height:16px;width:51px;background:var(--navy);color:#fff;border-radius:2px;font-family:"Yanone Kaffeesatz",sans-serif;font-size:8px;display:flex;align-items:center;justify-content:center}

.news-title{top:808px;left:0;width:676px;text-align:center;font-family:"Yanone Kaffeesatz",sans-serif;font-weight:600;font-size:19px;color:#2d3b45}
.date-badge{width:17px;font-family:"Yanone Kaffeesatz",sans-serif;text-align:center;font-size:6px}
.date-badge .month{background:var(--date-orange);color:#fff;height:11px;line-height:11px}
.date-badge .day{color:#333;line-height:8px}
.news-item h4{font-family:"Yanone Kaffeesatz",sans-serif;font-weight:600;font-size:12.6px;color:#2d3b45;white-space:nowrap}
.news-item h4.highlight{color:var(--orange)}
.news-item p{font-family:"Yanone Kaffeesatz",sans-serif;font-size:8px;line-height:12.5px;color:#333;width:160px;margin-top:6px;text-indent:12px}

.newsletter{left:158px;top:969px;width:361px;height:40px;border-radius:2px;background:linear-gradient(var(--teal-top),var(--teal-bottom));box-shadow:0 1px 2px rgba(0,0,0,.25)}
.newsletter .label{position:absolute;left:9px;top:7px;font-family:"Nunito",sans-serif;font-weight:800;font-size:17px;color:#fff;letter-spacing:.3px}
.newsletter .field{position:absolute;left:194px;top:8px;width:158px;height:24px;background:#fff;border:2px solid #cfe9e5;border-radius:3px;font-family:Georgia,serif;font-style:italic;font-size:11px;color:#aaa;padding:3px 6px}

.footer{left:0;top:1030px;width:676px;height:143px;background:var(--footer);border-top:3px solid #555;color:var(--footer-text)}
.footer h5{position:absolute;top:16px;font-size:7.5px;font-weight:700;color:#fff}
.footer .about{position:absolute;left:120px;top:34px;width:170px;font-size:5.4px;line-height:9.6px}
.footer .sign{position:absolute;left:203px;top:97px;font-size:5.6px}
.social{position:absolute;left:329px;top:33px;list-style:none;font-size:6px}
.social li{display:flex;align-items:center;gap:7px;height:20px}
.social .dot{width:13px;height:13px;border-radius:50%;background:#fff}
.social .on{color:var(--link-blue)}
.social .on .dot{background:var(--link-blue)}
.contact{position:absolute;left:479px;top:34px;list-style:none;font-size:5.8px}
.contact li{height:16px;display:flex;align-items:center;gap:6px}
.contact li.indent{padding-left:14px}
.contact .ico{width:8px;display:inline-flex;justify-content:center}
.contact a{color:var(--link-blue);text-decoration:none}
.bottom-bar{left:0;top:1173px;width:676px;height:27px;background:var(--footer-base);color:#ddd;font-size:6px}
.bottom-bar span{position:absolute;top:10px}
</style>
</head>
<body>

<header>
  <div class="abs logo">CareVaultPlus</div>
  <div class="abs top-links">
    <span>Log in</span><span class="sep">|</span>
    <span class="phone-icon"><svg width="7" height="7" viewBox="0 0 10 10"><path d="M2 1l2 2-1 1.5c.8 1.3 1.7 2.2 3 3L7.5 6l2 2-1.5 1.5C4.5 9 1 5.5.5 2.5z" fill="#fff"/></svg></span>
    <span>Call us&nbsp; 012-555-0147</span>
  </div>
  <nav class="abs main-nav">
    <a class="active" style="left:270px">HOME</a>
    <a style="left:321px">ABOUT US</a>
    <a style="left:390px">FAQ</a>
    <a style="left:432px">CONTACT US</a>
  </nav>
</header>

<section class="hero-slider">
  <div class="abs hero" role="img" aria-label="Photo of three smiling friends giving a thumbs up"></div>
  <svg class="abs slider-arrow" style="left:50px" viewBox="0 0 30 38"><path d="M22 4L8 19l14 15" fill="none" stroke="#ccc" stroke-width="5"/></svg>
  <svg class="abs slider-arrow" style="left:598px" viewBox="0 0 30 38"><path d="M8 4l14 15L8 34" fill="none" stroke="#ccc" stroke-width="5"/></svg>
  <div class="abs slider-dots"><span></span><span class="current"></span><span></span><span></span></div>
</section>

<section class="intro">
  <h1 class="abs tagline">Shop with confidence knowing<br><span class="brand">CareVaultPlus</span> is there</h1>
  <div class="abs cta">Lean more</div>
  <div class="abs divider"></div>
</section>

<section class="features">
  <div class="abs feature" style="left:81px">
    <div class="ring"><svg width="22" height="26" viewBox="0 0 22 26"><path d="M5 11V7a6 6 0 0112 0v4" fill="none" stroke="#111" stroke-width="3"/><path d="M2 11h18v8l-9 6-9-6z" fill="#111"/><circle cx="11" cy="16" r="2" fill="#fff"/><rect x="10" y="16" width="2" height="4" fill="#fff"/></svg></div>
    <h3>Valuable purchase protection</h3>
    <p>Get 5 unique ways to get more out of the things you buy:*</p>
    <ul>
      <li>Warranty extension</li>
      <li>Repair bill rebate</li>
      <li>Product return guarantee</li>
      <li>Price protection</li>
      <li>Restocking fee reimbursement</li>
    </ul>
  </div>
  <div class="abs feature" style="left:251px">
    <div class="ring"><svg width="28" height="24" viewBox="0 0 28 24"><path d="M6 2h20v18H6z" fill="#111"/><path d="M2 8h14v14H2z" fill="#111" stroke="#fff" stroke-width="1.5"/><rect x="7" y="13" width="4" height="5" fill="#fff"/></svg></div>
    <h3>Easy claims process</h3>
    <p>Using CareVaultPlus has never been easier. Just send us copies, scans or photos of your receipts — we'll store them securely online. Then download what you need and submit your claim online.</p>
  </div>
  <div class="abs feature" style="left:422px">
    <div class="ring"><svg width="28" height="24" viewBox="0 0 28 24"><path d="M2 2v20h22" fill="none" stroke="#111" stroke-width="1.5"/><rect x="5" y="10" width="2.5" height="10" fill="#111"/><rect x="9" y="7" width="2.5" height="13" fill="#111"/><rect x="13" y="12" width="2.5" height="8" fill="#111"/><circle cx="19" cy="9" r="5" fill="none" stroke="#111" stroke-width="2"/><path d="M22.5 12.5L26 17" stroke="#111" stroke-width="2.5"/></svg></div>
    <h3>One low monthly fee</h3>
    <p>Get a $ bonus rebate each calendar quarter to use on home electronics and appliance purchases.</p>
  </div>
  <div class="abs small-btn" style="left:192px;top:744px">Read more...</div>
  <div class="abs small-btn" style="left:351px;top:744px">Read more...</div>
  <div class="abs small-btn" style="left:524px;top:744px">Read more...</div>
</section>

<section class="latest-news">
  <h2 class="abs news-title">Latest News</h2>
  <div class="abs date-badge" style="left:118px;top:847px"><div class="month">July</div><div class="day">1</div></div>
  <article class="abs news-item" style="left:146px;top:844px">
    <h4>Fusce id suscipit lorem, ut malesuada</h4>
    <p>Praesent blandit turpis dui, eu consectetur nulla dignissim sit amet. Aliquam faucibus iaculis orci, a viverra ligula vulputate non</p>
  </article>
  <div class="abs small-btn" style="left:232px;top:912px;width:54px">Read More.....</div>

  <div class="abs date-badge" style="left:375px;top:847px"><div class="month">July</div><div class="day">3</div></div>
  <article class="abs news-item" style="left:403px;top:844px">
    <h4 class="highlight">Mauris sapien ante, adipiscing alim</h4>
    <p>Praesent blandit turpis dui, eu consectetur nulla dignissim sit amet. Aliquam faucibus iaculis orci, a viverra ligula vulputate non</p>
  </article>
  <div class="abs small-btn" style="left:488px;top:912px;width:54px">Read More.....</div>
</section>

<section class="abs newsletter">
  <span class="label">get our newsletter</span>
  <div class="field">Enter e-mail Address</div>
</section>

<footer class="abs footer">
  <h5 style="left:120px">More About Company</h5>
  <p class="about">Lorem ipsum dolor sit amet, consectetur adipiscing elit. Duis dapibus rhoncus purus, quis aliquet urna vehicula eu. Maecenas velit orci, volutpat sed posuere eu, vehicula eu tellus. Pellentesque sem sapien, aliquet id rhoncus eget, interdum vitae ligula.</p>
  <p class="sign">- Daniel Rowe, <b>CEO</b></p>

  <h5 style="left:329px">Keep Connected</h5>
  <ul class="social">
    <li><span class="dot"></span>Like us on FriendHub</li>
    <li><span class="dot"></span>Follow us on Chirper</li>
    <li class="on"><span class="dot"></span>Add us on CircleNet</li>
    <li><span class="dot"></span>Follow us on WorkLink</li>
    <li><span class="dot"></span>Subscribe to our RSS</li>
  </ul>

  <h5 style="left:479px">Contact Information</h5>
  <ul class="contact">
    <li><span class="ico"><svg width="8" height="7" viewBox="0 0 8 7"><path d="M4 0L0 3.5h1V7h2.2V5h1.6v2H7V3.5h1z" fill="#fff"/></svg></span>Member Services</li>
    <li class="indent">14 Harbour Lane</li>
    <li class="indent">Eastfield, EF2 9QA</li>
    <li><span class="ico"><svg width="5" height="8" viewBox="0 0 5 8"><rect x=".5" y=".5" width="4" height="7" rx="1" fill="none" stroke="#fff"/></svg></span><b>0800 555 0199</b></li>
    <li><span class="ico"><svg width="8" height="6" viewBox="0 0 8 6"><rect width="8" height="6" fill="#fff"/><path d="M0 0l4 3.5L8 0" fill="none" stroke="#2b2b2b" stroke-width=".8"/></svg></span><a>hello@carevaultplus.example</a></li>
  </ul>
</footer>

<div class="abs bottom-bar">
  <span style="left:88px">Copyright @ 2014 CareVaultPlus. All rights reserved.</span>
  <span style="left:377px">Company Information</span>
  <span style="left:454px">|</span>
  <span style="left:466px">Privacy Policy</span>
  <span style="left:519px">|</span>
  <span style="left:531px">Terms &amp; Conditions</span>
</div>

</body>
</html>
```